Modern Lawfirm Business Card Design

We're looking for a business card to incorporate the newly created logo we had made.

Ideally looking for a law firm business card demonstrating, modern, minimalist, strong/bold design.

I'm open to any design honestly, but nothing "flashy".

Target Market(s)

Immigration law, family immigration, humanitarian, general legal

Industry/Entity Type

Law Firm

Contact Information for Business Card

Please use dummy information, name, street address, city, state, phone number, email, website.

Font styles to use
Serif
Sans Serif

Requirements
Must have
• Please use dummy information, name, street address, city, state, phone number, email, website.

```html
<!DOCTYPE html>
<html lang="en">
<head>
<meta charset="utf-8">
<title>Halvern – Business Card</title>
<link rel="stylesheet" href="https://fonts.googleapis.com/css2?family=Crimson+Text:wght@400;600;700&display=swap">
<style>
  :root {
    --backdrop: #ebebeb;
    --card-white: #f8f8f7;
    --brand-blue: #1f6aa5;
    --brand-blue-light: #4b8fbd;
    --brand-blue-deep: #22629a;
    --ink: #3a3a3a;
    --ink-soft: #555555;
    --white: #ffffff;
  }
  * { box-sizing: border-box; margin: 0; padding: 0; }
  html, body {
    width: 1200px; height: 720px; overflow: hidden;
    background: var(--backdrop);
    font-family: "Crimson Text", Georgia, serif;
  }
  .canvas { position: relative; width: 1200px; height: 720px; }

  .card { position: absolute; top: 241px; width: 420px; height: 240px; overflow: hidden; }

  /* Front */
  .card-front {
    left: 147px;
    background: linear-gradient(225deg, var(--brand-blue-light) 0%, var(--brand-blue) 55%, var(--brand-blue-deep) 100%);
  }
  .front-wordmark {
    position: absolute; left: 0; right: 0; top: 100px;
    display: flex; align-items: center; justify-content: center; gap: 8px;
    color: var(--white); font-weight: 600; font-size: 30px; letter-spacing: 1px; line-height: 1;
  }
  .wordmark-square { width: 10px; height: 10px; background: var(--white); }

  /* Back */
  .card-back { left: 633px; background: var(--card-white); }
  .accent-bar { position: absolute; left: 32px; top: 0; width: 4px; height: 134px; background: var(--brand-blue); }
  .bottom-band { position: absolute; left: 0; right: 0; bottom: 0; height: 10px; background: var(--brand-blue); }
  .side-dash { position: absolute; right: 0; top: 195px; width: 28px; height: 5px; background: var(--brand-blue-deep); }

  .holder-name {
    position: absolute; left: 55px; top: 40px;
    color: var(--brand-blue); font-weight: 700; font-size: 19px; line-height: 1;
  }
  .holder-credentials {
    position: absolute; left: 55px; top: 66px;
    color: var(--brand-blue); font-size: 15px; line-height: 1;
  }
  .back-wordmark {
    position: absolute; right: 37px; top: 40px;
    display: flex; align-items: center; gap: 6px;
    color: var(--brand-blue); font-weight: 600; font-size: 22px; letter-spacing: 0.5px; line-height: 1;
  }
  .back-wordmark .wordmark-square { width: 8px; height: 8px; background: var(--brand-blue); }

  .contact {
    position: absolute; display: flex; align-items: center; gap: 5px;
    color: var(--ink); font-size: 12px; line-height: 1;
  }
  .contact svg { width: 9px; height: 10px; fill: var(--ink-soft); flex: none; }
  .contact-address { left: 28px; top: 138px; }
  .contact-phone { left: 30px; top: 166px; }
  .contact-fax { left: 141px; top: 166px; }
  .contact-email { left: 30px; top: 191px; }
  .contact-web { right: 41px; top: 191px; font-size: 13px; }
</style>
</head>
<body>
<main class="canvas">
  <section class="card card-front" aria-label="Card front">
    <div class="front-wordmark"><span class="wordmark-square"></span>HALVERN</div>
  </section>

  <section class="card card-back" aria-label="Card back">
    <div class="accent-bar"></div>
    <h1 class="holder-name">Lucas Halvern</h1>
    <p class="holder-credentials">J.D., LL.M.</p>
    <div class="back-wordmark"><span class="wordmark-square"></span>HALVERN</div>

    <p class="contact contact-address">
      <svg viewBox="0 0 10 12" aria-hidden="true"><path d="M5 0a4 4 0 0 0-4 4c0 3 4 8 4 8s4-5 4-8a4 4 0 0 0-4-4zm0 5.5A1.5 1.5 0 1 1 5 2.5a1.5 1.5 0 0 1 0 3z"/></svg>
      14 Bramble Street, Kelwood NSW 2071
    </p>
    <p class="contact contact-phone">
      <svg viewBox="0 0 10 10" aria-hidden="true"><path d="M2 0l2 2.5-1 1.2c.6 1.3 1.6 2.3 2.9 2.9l1.2-1L10 7.6 8.7 9.6C4.2 9.6.4 5.8.4 1.3z"/></svg>
      (400) 555 0142
    </p>
    <p class="contact contact-fax">
      <svg viewBox="0 0 10 10" aria-hidden="true"><path d="M2 0h5l1.5 1.5V10H2z"/></svg>
      (400) 555 0143
    </p>
    <p class="contact contact-email">
      <svg viewBox="0 0 12 8" aria-hidden="true" style="width:11px;height:8px"><path d="M0 0h12v1L6 4.5 0 1zM0 2.2l6 3.5 6-3.5V8H0z"/></svg>
      info@halvern.com
    </p>
    <p class="contact contact-web">www.halvern.com</p>

    <div class="side-dash"></div>
    <div class="bottom-band"></div>
  </section>
</main>
</body>
</html>
```